Qasr nadim
Project: Qasr nadim
Qasr nadim - Construction
Creative Brief
Bright & Fun-filled
Omar Saleh Dawud عمر صالح داود
CEO المدير المفوض
Nadim Road - Iraq
CEO@Qasrnadim.example
www.qasrnadim.example

```html
<!DOCTYPE html>
<html lang="en">
<head>
<meta charset="utf-8">
<title>Qasr nadim — Business Card</title>
<link href="https://fonts.googleapis.com/css2?family=Open+Sans:ital,wght@0,400;0,600;0,700;1,400&family=Noto+Naskh+Arabic:wght@400;700&display=swap" rel="stylesheet">
<style>
  :root {
    --navy: #2a1f7a;
    --navy-deep: #1c1560;
    --navy-light: #4a3f9e;
    --red: #b3242c;
    --red-deep: #8f1a20;
    --ink: #1d1a55;
    --grey: #555a66;
    --white: #ffffff;
    --backdrop: #e9eaee;
  }
  * { box-sizing: border-box; margin: 0; padding: 0; }
  html, body { width: 1200px; height: 871px; overflow: hidden; }
  body {
    background: var(--backdrop);
    font-family: "Open Sans", sans-serif;
    display: flex;
    flex-direction: column;
    align-items: center;
    justify-content: center;
    gap: 44px;
  }
  .card {
    position: relative;
    width: 580px;
    height: 332px;
    border-radius: 18px;
    overflow: hidden;
    box-shadow: 0 10px 30px rgba(20, 20, 40, 0.18);
  }

  /* Back side */
  .card--back {
    background: linear-gradient(125deg, var(--navy-deep) 0%, var(--navy) 45%, var(--navy-light) 55%, var(--navy) 70%, var(--navy-deep) 100%);
  }
  .card--back .brand-name {
    position: absolute;
    top: 130px; left: 0; right: 0;
    text-align: center;
    color: var(--white);
    font-weight: 700;
    font-size: 40px;
    letter-spacing: 2px;
  }
  .card--back .web {
    position: absolute;
    bottom: 24px; left: 0; right: 0;
    text-align: center;
    color: rgba(255,255,255,0.85);
    font-size: 13px;
    letter-spacing: 2px;
  }

  /* Front side */
  .card--front { background: linear-gradient(180deg, #ffffff 0%, #f1f1f4 100%); }
  .brand {
    position: absolute;
    left: 42px; top: 92px;
    display: flex;
    align-items: center;
    gap: 12px;
  }
  .brand-mark {
    width: 14px; height: 14px;
    background: var(--navy);
  }
  .brand-text {
    border-left: 2px solid var(--navy);
    padding-left: 10px;
    color: var(--navy);
  }
  .brand-arabic {
    font-family: "Noto Naskh Arabic", serif;
    font-size: 30px;
    line-height: 1.1;
    font-weight: 400;
    direction: rtl;
    text-align: left;
  }
  .brand-latin {
    font-size: 15px;
    font-weight: 400;
    letter-spacing: 1px;
  }

  .contact {
    position: absolute;
    left: 340px; top: 62px;
    color: var(--grey);
  }
  .person-name { color: var(--ink); font-weight: 700; font-size: 18px; line-height: 1.2; }
  .person-name-ar { font-family: "Noto Naskh Arabic", serif; color: var(--ink); font-size: 14px; font-weight: 700; line-height: 1.3; direction: rtl; text-align: left; }
  .role { color: var(--red); font-size: 13px; line-height: 1.3; }
  .role-ar { font-family: "Noto Naskh Arabic", serif; color: var(--red); font-size: 13px; line-height: 1.4; direction: rtl; text-align: left; }
  .location { font-size: 13px; margin-top: 14px; }
  .line { display: flex; align-items: center; gap: 8px; font-size: 13px; margin-top: 8px; }
  .line svg { width: 14px; height: 14px; flex: none; }

  .band { position: absolute; left: 0; bottom: 0; width: 580px; height: 68px; }
  .band-web {
    position: absolute;
    right: 26px; bottom: 12px;
    color: var(--white);
    font-style: italic;
    font-size: 14px;
    letter-spacing: 1px;
  }
</style>
</head>
<body>

  <section class="card card--back">
    <div class="brand-name">QASR NADIM</div>
    <div class="web">www.qasrnadim.example</div>
  </section>

  <section class="card card--front">
    <div class="brand">
      <span class="brand-mark"></span>
      <div class="brand-text">
        <div class="brand-arabic">قصر نديم</div>
        <div class="brand-latin">QASR NADIM</div>
      </div>
    </div>

    <div class="contact">
      <div class="person-name">Omar Saleh Dawud</div>
      <div class="person-name-ar">عمر صالح داود</div>
      <div class="role">CEO</div>
      <div class="role-ar">المدير المفوض</div>
      <div class="location">Nadim Road - Iraq</div>
      <div class="line">
        <svg viewBox="0 0 14 14" aria-hidden="true"><rect x="3.5" y="0.8" width="7" height="12.4" rx="1.4" fill="none" stroke="#1d1a55" stroke-width="1.4"/><circle cx="7" cy="11" r="0.8" fill="#1d1a55"/></svg>
        <span>964-7700001234</span>
      </div>
      <div class="line">
        <svg viewBox="0 0 14 14" aria-hidden="true"><rect x="0.8" y="3" width="12.4" height="8.5" fill="none" stroke="#1d1a55" stroke-width="1.3"/><path d="M1 3.4 L7 8 L13 3.4" fill="none" stroke="#1d1a55" stroke-width="1.3"/></svg>
        <span>CEO@Qasrnadim.example</span>
      </div>
    </div>

    <svg class="band" viewBox="0 0 580 68" aria-hidden="true">
      <defs>
        <linearGradient id="navyShine" x1="0" y1="0" x2="1" y2="0">
          <stop offset="0" stop-color="#1c1560"/>
          <stop offset="0.45" stop-color="#2a1f7a"/>
          <stop offset="0.6" stop-color="#5448a8"/>
          <stop offset="0.75" stop-color="#2a1f7a"/>
          <stop offset="1" stop-color="#1c1560"/>
        </linearGradient>
        <linearGradient id="redFade" x1="0" y1="0" x2="0" y2="1">
          <stop offset="0" stop-color="#b3242c"/>
          <stop offset="1" stop-color="#8f1a20"/>
        </linearGradient>
      </defs>
      <polygon points="0,0 580,30 580,68 0,68" fill="url(#navyShine)"/>
      <polygon points="352,18 580,30 580,68 322,68" fill="url(#redFade)"/>
      <polygon points="352,18 358,18 328,68 322,68" fill="#ffffff"/>
    </svg>
    <div class="band-web">www.qasrnadim.example</div>
  </section>

</body>
</html>
```